Brisk Ripple Card Design Project

Selling water treatment/filters to residential homeswould like some kind of water design or pic used....
We sale water softeners and drinking filters
In-home sales
I included one picture of what I like on the back.... But I hope we find something better.... So I don't necessarily want to use that pic, but something close....

I am looking for this business card to be very professional, making it look like a very solid, we financed company.

Target Market(s)

Middle to upper class home owners

Industry/Entity Type

Water Purification

Contact Information for Business Card

Paul GrantCell: 801-361-7154Office: 801-830-8055www.BriskRipple.net

Font styles to use
Serif

Colors
3277b5
33a6d7

Requirements
Nice to have
• Some kind of water "splash's" or flowing "clean" mountain water if possible

```html
<!DOCTYPE html>
<html lang="en">
<head>
<meta charset="utf-8">
<title>Brisk Ripple Business Card</title>
<link rel="stylesheet" href="https://fonts.googleapis.com/css2?family=Bodoni+Moda:wght@700;800&family=Arimo:wght@400&display=swap">
<style>
  :root {
    --page-bg: #e6e6e6;
    --card-white: #ffffff;
    --brand-blue: #2b368c;
    --ink-black: #0a0a0a;
    --drop-light: #f4f6f8;
    --drop-mid: #dde2e7;
  }
  html, body {
    margin: 0;
    padding: 0;
    width: 1189px;
    height: 1200px;
    overflow: hidden;
    background: var(--page-bg);
  }
  .canvas {
    position: relative;
    width: 1189px;
    height: 1200px;
  }
  .card {
    position: absolute;
    left: 140px;
    width: 1124px;
    height: 642px;
    background: var(--card-white);
    transform-origin: 0 0;
    transform: scale(0.8158);
    overflow: hidden;
    box-shadow: 0 6px 16px rgba(0,0,0,0.25);
  }
  .card--front { top: 45px; }
  .card--back { top: 623px; }

  .front-shapes {
    position: absolute;
    inset: 0;
  }
  .brand-name {
    position: absolute;
    left: 0;
    right: 0;
    top: 126px;
    margin: 0;
    text-align: center;
    font-family: "Bodoni Moda", "Didot", serif;
    font-weight: 800;
    font-size: 96px;
    line-height: 1;
    color: var(--ink-black);
  }
  .person-name {
    position: absolute;
    left: 104px;
    top: 474px;
    margin: 0;
    font-family: "Bodoni Moda", "Didot", serif;
    font-weight: 700;
    font-size: 70px;
    line-height: 1;
    color: var(--card-white);
  }
  .divider {
    position: absolute;
    left: 567px;
    top: 433px;
    width: 3px;
    height: 153px;
    background: var(--card-white);
  }
  .contact-list {
    position: absolute;
    left: 592px;
    top: 440px;
    margin: 0;
    padding: 0;
    list-style: none;
  }
  .contact-item {
    display: flex;
    align-items: center;
    height: 46px;
    font-family: "Arimo", Arial, sans-serif;
    font-size: 35px;
    color: var(--card-white);
  }
  .contact-icon {
    width: 30px;
    height: 26px;
    margin-right: 48px;
    flex: none;
  }

  .droplet-field {
    position: absolute;
    inset: 0;
    background:
      radial-gradient(ellipse at 50% 50%, var(--card-white) 0%, var(--drop-light) 55%, var(--drop-mid) 100%);
  }
  .web-address {
    position: absolute;
    left: 0;
    right: 0;
    top: 262px;
    margin: 0;
    text-align: center;
    font-family: "Bodoni Moda", "Didot", serif;
    font-weight: 800;
    font-size: 104px;
    line-height: 1;
    color: var(--brand-blue);
  }
</style>
</head>
<body>
<main class="canvas">

  <section class="card card--front">
    <svg class="front-shapes" width="1124" height="642" viewBox="0 0 1124 642">
      <polygon fill="var(--brand-blue)" points="0,288 133,360 993,360 1124,290 1124,642 0,642"/>
      <polygon fill="var(--ink-black)" points="55,302 133,330 993,330 1075,302 995,348 128,348"/>
    </svg>
    <h1 class="brand-name">Brisk Ripple</h1>
    <p class="person-name">Dean Morlow</p>
    <div class="divider"></div>
    <ul class="contact-list">
      <li class="contact-item">
        <svg class="contact-icon" viewBox="0 0 30 26" aria-label="Phone">
          <rect width="30" height="26" rx="3" fill="var(--card-white)"/>
          <path d="M7 11 Q15 4 23 11 L21 13 L18 11 L12 11 L9 13 Z" fill="var(--brand-blue)"/>
          <rect x="10" y="13" width="10" height="7" rx="1.5" fill="var(--brand-blue)"/>
        </svg>
        801-472-9306
      </li>
      <li class="contact-item">
        <svg class="contact-icon" viewBox="0 0 30 26" aria-label="Office">
          <rect width="30" height="26" rx="3" fill="var(--card-white)"/>
          <rect x="9" y="4" width="12" height="6" fill="var(--brand-blue)"/>
          <rect x="6" y="11" width="18" height="8" rx="1" fill="var(--brand-blue)"/>
          <rect x="10" y="17" width="10" height="5" fill="var(--brand-blue)"/>
        </svg>
        801-594-2217
      </li>
      <li class="contact-item">
        <svg class="contact-icon" viewBox="0 0 30 26" aria-label="Email">
          <rect width="30" height="26" rx="3" fill="var(--card-white)"/>
          <rect x="6" y="7" width="18" height="12" fill="var(--brand-blue)"/>
          <path d="M6 7 L15 14 L24 7 M6 19 L12 13 M24 19 L18 13" stroke="var(--card-white)" stroke-width="1.6" fill="none"/>
        </svg>
        Dean@BriskRipple.net
      </li>
    </ul>
  </section>

  <section class="card card--back">
    <div class="droplet-field" role="img" aria-label="Scattered clear water droplets across a white surface"></div>
    <p class="web-address">BriskRipple.net</p>
  </section>

</main>
</body>
</html>
```